Flyer Design for PickUp and Delivery -- 1

I need some graphic design.
Flyer for an upstart business.
Laundry Service: - Dry Cleaning - Fluff and fold - Wash and press.
Laundry Pick-up and Delivery. Its like Zolt but for laundry.
- No picture of a girl holding a laundry basket please.
Include Phone #
Email
Website

here are some inspiration
Check out Sudsy Cubby -- Sudsycubbyx.com

http://www.pagemintery.com/Downloads/PDF/Preview/KT4471902X-PREVIEW.pdf

http://www.tidyleafletz.com/flyers/laundry-flyer.html

http://www.snapvaultimg.com/similar-583920114/stock-vector-laundry-service-flyer-poster-template.html?page=1&inline=402719385

http://www.wellnourmag.com/eco/eco-home/clean-up-your-laundry-habits

```html
<!DOCTYPE html>
<html lang="en">
<head>
<meta charset="utf-8">
<title>Laundry Pick-up and Delivery Flyer</title>
<link rel="stylesheet" href="https://fonts.googleapis.com/css2?family=Roboto+Condensed:ital,wght@0,500;0,700;1,800&display=swap">
<style>
  :root {
    --page-bg: #ececec;
    --sky-top: #2f7fd4;
    --sky-mid: #8cc3ee;
    --sky-low: #e8f4fc;
    --paper: #ffffff;
    --navy: #3a379a;
    --navy-text: #2f2c8e;
    --white: #ffffff;
    --illus-blue: #9fc3e6;
    --illus-van: #e4e6f2;
  }
  * { box-sizing: border-box; margin: 0; padding: 0; }
  html, body {
    width: 1059px; height: 1200px; overflow: hidden;
    background: var(--page-bg);
    font-family: "Roboto Condensed", "Arial Narrow", sans-serif;
  }
  .flyer {
    position: absolute; left: 134px; top: 33px;
    width: 790px; height: 1134px;
    background: var(--paper);
    overflow: hidden;
    box-shadow: 0 6px 24px rgba(0,0,0,.18);
  }
  .sky {
    position: absolute; left: 0; top: 0; width: 100%; height: 400px;
    background: linear-gradient(180deg, var(--sky-top) 0%, var(--sky-mid) 38%, var(--sky-low) 62%, var(--paper) 80%);
  }
  .headline {
    position: absolute; left: 0; top: 38px; width: 100%;
    text-align: center; color: var(--white);
    font-weight: 800; font-style: italic;
    font-size: 84px; line-height: 80px; letter-spacing: 0.5px;
    text-transform: uppercase;
  }
  .hero-art {
    position: absolute; left: 175px; top: 226px; width: 376px; height: 150px;
    border-radius: 10px;
    background: linear-gradient(90deg, #5a9bd8 0%, #c9d8ea 50%, #7d8fb8 100%);
  }
  .van-art {
    position: absolute; left: 138px; top: 402px; width: 526px; height: 260px;
    border-radius: 24px;
    background: linear-gradient(180deg, var(--illus-van) 0%, #d3d6ea 70%, #b9bcd8 100%);
  }
  .services {
    position: absolute; left: 102px; top: 685px; width: 590px; height: 170px;
    background: var(--navy); border-radius: 14px;
    color: var(--white);
    display: flex; align-items: center; padding: 0 22px;
  }
  .services-title {
    font-weight: 700; font-size: 56px; line-height: 58px;
    text-transform: uppercase; margin-right: 34px;
  }
  .services-list { list-style: none; }
  .services-list li {
    display: flex; align-items: center;
    font-weight: 500; font-size: 39px; line-height: 48px;
  }
  .tick { width: 30px; height: 30px; margin-right: 14px; flex: none; }
  .contact-band {
    position: absolute; left: 0; top: 872px; width: 100%; height: 166px;
    background: var(--navy); color: var(--white); text-align: center;
  }
  .phone {
    display: block; font-weight: 700; font-size: 90px; line-height: 90px;
    margin-top: 12px; letter-spacing: 1px;
  }
  .email {
    display: flex; justify-content: center; align-items: center;
    font-weight: 500; font-size: 33px; margin-top: 8px;
  }
  .envelope { width: 40px; height: 28px; margin-right: 12px; }
  .website {
    position: absolute; left: 0; top: 1052px; width: 100%;
    text-align: center; color: var(--navy-text);
    font-weight: 700; font-size: 37px;
  }
</style>
</head>
<body>
<main class="flyer">
  <div class="sky"></div>
  <h1 class="headline">Laundry Pick-up<br>and Delivery</h1>

  <div class="hero-art" role="img" aria-label="Illustration of a basket of messy laundry with an arrow pointing to a neat stack of folded shirts"></div>
  <div class="van-art" role="img" aria-label="Illustration of a white delivery van decorated with a shirt and washing machine"></div>

  <section class="services">
    <h2 class="services-title">Laundry<br>Service:</h2>
    <ul class="services-list">
      <li><svg class="tick" viewBox="0 0 30 30"><rect x="2" y="4" width="22" height="22" fill="none" stroke="#fff" stroke-width="2.5"/><path d="M7 14 L13 20 L27 4" fill="none" stroke="#fff" stroke-width="3"/></svg>Dry Cleaning</li>
      <li><svg class="tick" viewBox="0 0 30 30"><rect x="2" y="4" width="22" height="22" fill="none" stroke="#fff" stroke-width="2.5"/><path d="M7 14 L13 20 L27 4" fill="none" stroke="#fff" stroke-width="3"/></svg>Fluff and fold</li>
      <li><svg class="tick" viewBox="0 0 30 30"><rect x="2" y="4" width="22" height="22" fill="none" stroke="#fff" stroke-width="2.5"/><path d="M7 14 L13 20 L27 4" fill="none" stroke="#fff" stroke-width="3"/></svg>Wash and press</li>
    </ul>
  </section>

  <section class="contact-band">
    <span class="phone">472-472-472</span>
    <span class="email">
      <svg class="envelope" viewBox="0 0 40 28"><rect x="1" y="1" width="38" height="26" fill="#fff"/><path d="M1 1 L20 16 L39 1" fill="none" stroke="#3a379a" stroke-width="2.5"/></svg>
      hello@freshrunlaundry.com
    </span>
  </section>

  <p class="website">www.freshrunlaundry.com</p>
</main>
</body>
</html>
```